Sleek business card design for digital agency.

Brief document attached for detailed description and inspiration. Looking for a minimalist sleek, cool, modern business card design.

Industry/Entity Type

Digital

```html
<!DOCTYPE html>
<html lang="en">
<head>
<meta charset="utf-8">
<title>Tidewater Labs – Business Card</title>
<link rel="stylesheet" href="https://fonts.googleapis.com/css2?family=Mulish:wght@400;600;700&display=swap">
<style>
  :root {
    --backdrop: #2b2624;
    --card: #1c1a1f;
    --logo-ink: #0d0c0e;
    --logo-ink-back: #060507;
    --text-light: #f4f4f6;
    --accent: #2ea3dc;
    --font-main: "Mulish", "Century Gothic", sans-serif;
  }
  * { margin: 0; padding: 0; box-sizing: border-box; }
  html, body { width: 1200px; height: 1181px; overflow: hidden; }
  body {
    background: var(--backdrop);
    font-family: var(--font-main);
    position: relative;
  }
  .card {
    position: absolute;
    top: 252px;
    width: 385px;
    height: 667px;
    background: var(--card);
    overflow: hidden;
  }
  .card--back { left: 170px; }
  .card--front { left: 645px; }

  .card__artwork {
    position: absolute;
    inset: 0;
    width: 100%;
    height: 100%;
  }
  .wordmark {
    position: absolute;
    font-family: var(--font-main);
    font-weight: 700;
    color: var(--logo-ink);
    white-space: nowrap;
  }
  .card--back .wordmark {
    left: 222px;
    top: 604px;
    font-size: 19px;
    line-height: 24px;
    color: var(--logo-ink-back);
  }
  .card--front .wordmark {
    left: 58px;
    top: 60px;
    font-size: 30px;
    line-height: 36px;
    display: flex;
    align-items: center;
    gap: 10px;
  }
  .wordmark__dot {
    width: 26px;
    height: 26px;
    border-radius: 50%;
    background: var(--logo-ink);
    flex: none;
  }

  .identity {
    position: absolute;
    left: 85px;
    top: 296px;
    white-space: nowrap;
  }
  .identity__name {
    font-size: 27px;
    font-weight: 600;
    letter-spacing: 1.2px;
    color: var(--text-light);
    line-height: 34px;
  }
  .identity__role {
    font-size: 16.5px;
    font-weight: 600;
    letter-spacing: 1.8px;
    color: var(--accent);
    line-height: 20px;
  }
  .identity__note {
    font-size: 12.5px;
    font-weight: 700;
    color: var(--text-light);
    line-height: 22px;
  }

  .contact {
    position: absolute;
    left: 183px;
    top: 539px;
    list-style: none;
  }
  .contact__item {
    position: relative;
    padding-left: 21px;
    font-size: 11.5px;
    font-weight: 700;
    color: var(--text-light);
    line-height: 15.5px;
    letter-spacing: 0.3px;
    white-space: nowrap;
  }
  .contact__icon {
    position: absolute;
    left: 0;
    top: 3px;
    width: 10px;
    height: 10px;
    border-radius: 50%;
    background: var(--accent);
  }
  .contact__icon svg { display: block; width: 10px; height: 10px; }

  .website {
    position: absolute;
    left: 25px;
    top: 514px;
    transform-origin: 0 0;
    transform: rotate(90deg);
    font-size: 11px;
    line-height: 13px;
    font-weight: 700;
    color: var(--text-light);
    letter-spacing: 0.4px;
    white-space: nowrap;
  }
</style>
</head>
<body>

  <section class="card card--back">
    <svg class="card__artwork" viewBox="0 0 385 667" role="img" aria-label="Large dark lobster silhouette illustration spanning the card">
      <defs>
        <radialGradient id="artGlow" cx="35%" cy="55%" r="70%">
          <stop offset="0%" stop-color="#050506"/>
          <stop offset="60%" stop-color="#0c0b0e"/>
          <stop offset="100%" stop-color="#1c1a1f"/>
        </radialGradient>
      </defs>
      <rect width="385" height="667" fill="url(#artGlow)"/>
    </svg>
    <div class="wordmark">Tidewater Labs</div>
  </section>

  <section class="card card--front">
    <div class="wordmark"><span class="wordmark__dot"></span>Tidewater Labs</div>

    <div class="identity">
      <h1 class="identity__name">Daniel Hartley</h1>
      <p class="identity__role">Marketing Director</p>
      <p class="identity__note">Drink order: G&amp;T with cucumber</p>
    </div>

    <ul class="contact">
      <li class="contact__item"><span class="contact__icon"><svg viewBox="0 0 10 10"><path d="M5 2.2a1.8 1.8 0 0 0-1.8 1.8C3.2 5.4 5 7.8 5 7.8S6.8 5.4 6.8 4A1.8 1.8 0 0 0 5 2.2z" fill="#1c1a1f"/></svg></span>Level 2, 18 Marlow St<br>East Harbour NSW 2011</li>
      <li class="contact__item"><span class="contact__icon"><svg viewBox="0 0 10 10"><rect x="3.5" y="2" width="3" height="6" rx="0.6" fill="#1c1a1f"/></svg></span>0400 555 127</li>
      <li class="contact__item"><span class="contact__icon"><svg viewBox="0 0 10 10"><path d="M3 2.5l1.2 1.3-.6.8a4 4 0 0 0 1.8 1.8l.8-.6L7.5 7l-.6.8C4.8 7.8 2.2 5.2 2.2 3.1z" fill="#1c1a1f"/></svg></span>02 5550 1234</li>
      <li class="contact__item"><span class="contact__icon"></span>dhartley@tidewaterlabs.com</li>
      <li class="contact__item"><span class="contact__icon"></span>@dhartley81</li>
      <li class="contact__item"><span class="contact__icon"></span>social.example/TidewaterLabs</li>
    </ul>

    <p class="website">www.tidewaterlabs.com</p>
  </section>

</body>
</html>
```